Modern Catering Company needs Letterhead Design

We need a letterhead design that will make effective use of the corporate logo and color scheme, along with careful typography, helps this letterhead design communicate the brand well. We do have a corporate logo, however feel free to enhance the color scheme with gold and purple. We are serving a very upscale clientele so the letterhead has to reflect elegance, professionalism, cleanliness, and modern style. We are branding the company so the letterhead and business cards must fit the brand story. There should be no cartoonish elements in the design and we are looking for sharper lines.

Target Market(s)

Businesses and upscale clientele

Industry/Entity Type

Catering

Contact Information for Business Card

while this design can have any number of quirks and distinctions, it needs to be cohesive with the entire brand story clean, professional but edgy

Requirements
Must have
• must have good and carefully placement of it’s logo and where you place the text or the message. Colors blue, very deep purple, jewel tones not pastels, gold. Blue must be the primary color you may accent with purple or gold. Contact information is as follows: Co-Owners/ Chefs: R. Hollowmere & L. Brandt, phone: 414-555-0182 email:Contact@orchardtablecatering.example, address: 6127 W Larkspur Hollow Rd, Milwaukee, WI 53299
Should not have
• pastel colors, Do not add the BBQ information to the letterhead or business card it was a mistake by the previous designer.

```html
<!DOCTYPE html>
<html lang="en">
<head>
<meta charset="utf-8">
<title>Orchard Table Catering – Business Card</title>
<link rel="stylesheet" href="https://fonts.googleapis.com/css2?family=Open+Sans:wght@400;600;700&display=swap">
<style>
  :root {
    --stage: #ecebe8;
    --brand-blue: #1a6fe8;
    --brand-blue-deep: #0f56c9;
    --brand-purple: #4a2a8c;
    --card-white: #ffffff;
    --card-grey: #f1f1f3;
    --ink-grey: #5d5d66;
    --accent-red: #c0392b;
  }
  * { box-sizing: border-box; margin: 0; padding: 0; }
  html, body { width: 1200px; height: 843px; overflow: hidden; }
  body {
    background: var(--stage);
    font-family: "Open Sans", Arial, sans-serif;
    position: relative;
  }
  .card {
    position: absolute;
    top: 266px;
    width: 540px;
    height: 310px;
    border-radius: 22px;
    overflow: hidden;
    box-shadow: 0 8px 24px rgba(0,0,0,0.18);
  }
  /* Back side */
  .card--back {
    left: 40px;
    background: linear-gradient(160deg, #2d86f5 0%, var(--brand-blue) 55%, var(--brand-blue-deep) 100%);
    display: flex;
    flex-direction: column;
    align-items: center;
    justify-content: center;
    gap: 20px;
  }
  .back-name {
    font-size: 30px;
    font-weight: 600;
    letter-spacing: 2px;
    color: var(--accent-red);
    text-transform: uppercase;
  }
  .back-web {
    font-size: 17px;
    color: var(--card-white);
    letter-spacing: 0.5px;
  }
  /* Front side */
  .card--front {
    left: 620px;
    background: linear-gradient(180deg, var(--card-white) 40%, var(--card-grey) 100%);
  }
  .front-shape { position: absolute; inset: 0; }
  .brand {
    position: absolute;
    left: 34px;
    top: 58px;
    display: flex;
    align-items: center;
    gap: 12px;
  }
  .brand-dot {
    width: 16px; height: 16px;
    border-radius: 50%;
    background: var(--brand-purple);
  }
  .brand-name {
    font-size: 25px;
    font-weight: 600;
    line-height: 1.15;
    color: var(--brand-blue);
    text-transform: uppercase;
    letter-spacing: 1px;
  }
  .person {
    position: absolute;
    right: 30px;
    top: 62px;
    text-align: right;
    color: var(--card-white);
  }
  .person-name { font-size: 19px; font-weight: 700; }
  .person-role { font-size: 15px; }
  .contact-list {
    position: absolute;
    left: 34px;
    top: 172px;
    list-style: none;
    font-size: 14px;
    color: var(--ink-grey);
  }
  .contact-list li {
    display: flex;
    align-items: center;
    gap: 9px;
    height: 23px;
  }
  .contact-list svg { width: 13px; height: 13px; fill: var(--brand-blue); flex: none; }
  .address {
    position: absolute;
    right: 30px;
    bottom: 30px;
    text-align: right;
    font-size: 14px;
    line-height: 1.5;
    color: var(--ink-grey);
  }
</style>
</head>
<body>

<section class="card card--back" aria-label="Business card back">
  <p class="back-name">The Harbor Crown</p>
  <p class="back-web">www.orchardtablecatering.example</p>
</section>

<section class="card card--front" aria-label="Business card front">
  <svg class="front-shape" viewBox="0 0 540 310" preserveAspectRatio="none" aria-hidden="true">
    <path d="M150 0 C300 10 440 90 540 245 L540 0 Z" fill="var(--brand-blue)"/>
    <path d="M150 0 C300 10 440 90 540 245 L540 262 C440 104 300 18 150 0 Z" fill="var(--brand-purple)"/>
  </svg>

  <div class="brand">
    <span class="brand-dot"></span>
    <span class="brand-name">Orchard Table<br>Catering</span>
  </div>

  <div class="person">
    <p class="person-name">M. Carrow</p>
    <p class="person-role">CEO/Founder</p>
  </div>

  <ul class="contact-list">
    <li>
      <svg viewBox="0 0 24 24"><path d="M6.6 10.8a15 15 0 0 0 6.6 6.6l2.2-2.2c.3-.3.7-.4 1-.2 1.1.4 2.3.6 3.6.6.6 0 1 .4 1 1V20c0 .6-.4 1-1 1A17 17 0 0 1 3 4c0-.6.4-1 1-1h3.5c.6 0 1 .4 1 1 0 1.3.2 2.5.6 3.6.1.3 0 .7-.2 1z"/></svg>
      414-555-0182
    </li>
    <li>
      <svg viewBox="0 0 24 24"><path d="M2 5h20v14H2z M2 5l10 8 10-8" fill="none" stroke="var(--brand-blue)" stroke-width="2.4"/></svg>
      Contact@orchardtablecatering.example
    </li>
    <li>
      <svg viewBox="0 0 24 24"><circle cx="12" cy="12" r="10"/></svg>
      www.orchardtablecatering.example
    </li>
  </ul>

  <p class="address">6127 W Larkspur Hollow Rd<br>Milwaukee, WI 53299</p>
</section>

</body>
</html>
```